Rosquillas de Maíz y Queso

Necesitamos el de una bolsa que sea parcialmente transparente, para este producto, nuestra empresa se llama VELMORCO (Comercial Velmor), estamos ubicados en Honduras. Este un producto típico de Honduras, Este producto es para consumo masivo y será vendido en supermercados.
Adjunto ejemplos de empaques de este producto ya existentes.

Es nuestra primera vez, y queremos revisar bien los diseños, adicionalmente unos nos llegaron ayer y queremos unos pequeños cambios para poder decidir. Gracias

Clientes en supermercados

Panaderia

• La bolsa debe ser transparente con ventana para ver el producto
• Tiene que tener una ventana grande la bolsa o ser la mayor parte transparente para mostrar el producto

```html
<!DOCTYPE html>
<html lang="es">
<head>
<meta charset="UTF-8">
<title>Rosquillas de queso — VELMORCO</title>
<link rel="stylesheet" href="https://fonts.googleapis.com/css2?family=Kaushan+Script&family=Playfair+Display:wght@700;900&family=Open+Sans:wght@700&display=swap">
<style>
  :root {
    --bg: #b9b9b9;
    --red: #e31e26;
    --red-dark: #c3161d;
    --green: #0f9447;
    --green-light: #7dc242;
    --yellow: #f2e51b;
    --corn: #f3cf2a;
    --corn-deep: #e0a81a;
    --leaf: #5fb43a;
    --cream: #f7f1e4;
    --snack-light: rgba(246, 236, 214, 0.78);
    --snack-mid: rgba(222, 204, 170, 0.82);
    --badge: #1c1c1c;
    --white: #ffffff;
  }
  * { margin: 0; padding: 0; box-sizing: border-box; }
  html, body { width: 870px; height: 1200px; overflow: hidden; background: var(--bg); }
  .canvas { position: relative; width: 870px; height: 1200px; }
  .bag { position: absolute; left: 95px; top: 95px; width: 680px; height: 1010px; }
  .bag-art { position: absolute; inset: 0; }
  .product-window {
    position: absolute; left: 0; top: 60px; width: 680px; height: 885px;
    background:
      linear-gradient(115deg, rgba(255,255,255,0) 18%, rgba(255,255,255,0.45) 26%, rgba(255,255,255,0) 34%,
                      rgba(255,255,255,0) 66%, rgba(255,255,255,0.35) 74%, rgba(255,255,255,0) 82%),
      radial-gradient(circle at 25% 30%, var(--snack-light), var(--snack-mid) 75%),
      #9f9f9f;
    box-shadow: inset 0 0 40px rgba(255,255,255,0.55), inset 0 0 0 1px rgba(255,255,255,0.6);
  }
  .brand {
    position: absolute; left: 195px; top: 205px; width: 270px; text-align: center;
  }
  .brand-dot {
    display: block; width: 44px; height: 44px; margin: 0 auto 12px;
    border-radius: 50%; background: var(--cream);
  }
  .brand-name {
    display: block; white-space: nowrap;
    font-family: "Playfair Display", serif; font-weight: 700; font-size: 40px;
    color: var(--cream); letter-spacing: 0.5px; line-height: 1;
  }
  .flavor-label { position: absolute; left: 115px; top: 335px; width: 450px; height: 330px; }
  .flavor-title {
    position: absolute; left: 115px; top: 400px; width: 450px; text-align: center;
    font-family: "Kaushan Script", cursive; font-weight: 400;
  }
  .flavor-name { display: block; font-size: 76px; color: var(--white); line-height: 1; transform: rotate(-3deg); }
  .flavor-sub { display: block; font-size: 56px; color: var(--yellow); line-height: 1.15; margin-left: 110px; }
  .ingredients-art { position: absolute; left: 185px; top: 585px; width: 310px; height: 205px; }
  .seal {
    position: absolute; left: 285px; top: 778px; width: 96px; height: 96px; border-radius: 50%;
    background: var(--badge); border: 3px solid var(--white);
    display: flex; align-items: center; justify-content: center; text-align: center;
    font-family: "Open Sans", sans-serif; font-weight: 700; font-size: 8px; color: var(--white); line-height: 1.5;
  }
  .net-weight {
    position: absolute; left: 195px; top: 888px; width: 270px; text-align: center; white-space: nowrap;
    font-family: "Playfair Display", serif; font-weight: 900; font-size: 30px; line-height: 1; color: var(--cream);
  }
</style>
</head>
<body>
<main class="canvas">
  <section class="bag">
    <div class="product-window" role="img" aria-label="Ventana transparente que deja ver las rosquillas de maíz y queso"></div>
    <svg class="bag-art" width="680" height="1010" viewBox="0 0 680 1010">
      <rect class="band-top" x="0" y="0" width="680" height="60" fill="var(--red)"/>
      <rect class="band-center" x="195" y="60" width="270" height="885" fill="var(--red)"/>
      <rect class="band-bottom" x="0" y="945" width="680" height="65" fill="var(--red-dark)"/>
      <path class="wave-edge" fill="none" stroke="var(--green-light)" stroke-width="4"
        d="M195 60 q6 10 0 20 t0 20 t0 20 t0 20 t0 20 t0 20 t0 20 t0 20 t0 20 t0 20 t0 20 t0 20 t0 20 t0 20 t0 20 t0 20 t0 20 t0 20 t0 20 t0 20 t0 20 t0 20 t0 20 t0 20 t0 20 t0 20 t0 20 t0 20 t0 20 t0 20 t0 20 t0 20 t0 20 t0 20 t0 20 t0 20 t0 20 t0 20 t0 20 t0 20 t0 20 t0 20 t0 20 t0 20"/>
      <path class="wave-edge" fill="none" stroke="var(--green-light)" stroke-width="4"
        d="M465 60 q-6 10 0 20 t0 20 t0 20 t0 20 t0 20 t0 20 t0 20 t0 20 t0 20 t0 20 t0 20 t0 20 t0 20 t0 20 t0 20 t0 20 t0 20 t0 20 t0 20 t0 20 t0 20 t0 20 t0 20 t0 20 t0 20 t0 20 t0 20 t0 20 t0 20 t0 20 t0 20 t0 20 t0 20 t0 20 t0 20 t0 20 t0 20 t0 20 t0 20 t0 20 t0 20 t0 20 t0 20 t0 20"/>
    </svg>
    <div class="brand">
      <span class="brand-dot"></span>
      <span class="brand-name">VELMORCO</span>
    </div>
    <svg class="flavor-label" viewBox="0 0 450 330">
      <rect x="0" y="0" width="450" height="330" rx="110" fill="var(--green)"/>
      <rect x="14" y="14" width="422" height="302" rx="97" fill="none" stroke="var(--green-light)" stroke-width="2" stroke-dasharray="10 7"/>
    </svg>
    <h1 class="flavor-title">
      <span class="flavor-name">Rosquillas</span>
      <span class="flavor-sub">de queso</span>
    </h1>
    <svg class="ingredients-art" viewBox="0 0 310 205" role="img" aria-label="Ilustración de mazorcas de maíz con hojas y espigas de trigo">
      <defs>
        <linearGradient id="corn-fill" x1="0" y1="0" x2="0" y2="1">
          <stop offset="0" stop-color="var(--corn)"/>
          <stop offset="0.6" stop-color="var(--corn-deep)"/>
          <stop offset="1" stop-color="var(--leaf)"/>
        </linearGradient>
      </defs>
      <path d="M155 0 C200 10 260 40 300 80 C290 140 230 190 155 205 C80 190 20 140 10 80 C50 40 110 10 155 0 Z" fill="url(#corn-fill)"/>
    </svg>
    <div class="seal">PAN ARTESANAL<br>RECOMENDAMOS<br>REFRIGERAR</div>
    <p class="net-weight">Net Wt : 240 g</p>
  </section>
</main>
</body>
</html>
```